Business card design for new brand

We have recently rebranded and need a new business card template.

We are an insurance underwriting agency. All of our products are sold via other partner companies, so these are just to pass on our details to other organisations.

We would like to see designs that use the colour green (current stationary generally uses lime green (rgb 142,190,63) and forest green (0,154,79) to comply with our logo's colours. We are happy with other shades of green.

Business cards need to include our logo, as well as space for:
1. Full name
2. Qualifications (optional)
3. Title
4. Office number
5. Mobile number
6. Email address

Our logo is enclosed here.

```html
<!DOCTYPE html>
<html lang="en">
<head>
<meta charset="utf-8">
<title>Greenvale Underwriting – Business Card</title>
<link rel="stylesheet" href="https://fonts.googleapis.com/css2?family=Open+Sans:wght@400;600;700&display=swap">
<style>
  :root {
    --forest: #009a4f;
    --lime: #8ebe3f;
    --citron: #cfd92a;
    --ink: #111111;
    --paper: #ffffff;
    --backdrop: #e9ece8;
  }
  * { box-sizing: border-box; margin: 0; padding: 0; }
  html, body {
    width: 1200px; height: 913px; overflow: hidden;
    background: var(--backdrop);
    font-family: "Open Sans", Arial, sans-serif;
  }
  .sheet {
    width: 1200px; height: 913px;
    display: flex; flex-direction: column; align-items: center; justify-content: center;
    gap: 56px;
  }
  .card {
    position: relative;
    width: 600px; height: 343px;
    border-radius: 22px;
    overflow: hidden;
    box-shadow: 0 6px 18px rgba(0,0,0,0.18);
  }
  .card--front { background: var(--forest); }
  .card--back { background: var(--paper); }

  .brand {
    position: absolute;
    display: flex; align-items: center; gap: 14px;
    font-weight: 600;
    line-height: 1;
  }
  .brand__square { width: 34px; height: 34px; flex: none; }
  .brand__name { display: flex; flex-direction: column; gap: 6px; }
  .brand__main { font-size: 46px; letter-spacing: 0.5px; }
  .brand__sub { font-size: 20px; padding-left: 40px; }

  .card--front .brand { left: 130px; top: 126px; color: var(--paper); }
  .card--front .brand__square { background: var(--paper); }

  .card--back .brand { left: 40px; top: 48px; color: var(--ink); }
  .card--back .brand__main { font-size: 38px; }
  .card--back .brand__sub { font-size: 17px; padding-left: 34px; }
  .card--back .brand__square { width: 28px; height: 28px; background: var(--lime); }

  .wave { position: absolute; inset: 0; width: 100%; height: 100%; }

  .contact {
    position: absolute; right: 34px; top: 172px;
    text-align: right; color: var(--paper);
  }
  .contact__name {
    font-weight: 700; font-size: 22px; line-height: 1.25; color: var(--citron);
    text-transform: uppercase; letter-spacing: 0.3px;
  }
  .contact__title { font-size: 14px; margin-bottom: 10px; }
  .contact__list { list-style: none; font-size: 14px; line-height: 1.55; }
  .contact__list li { display: flex; justify-content: flex-end; align-items: center; gap: 8px; }
  .icon { width: 12px; height: 12px; flex: none; }
</style>
</head>
<body>
<main class="sheet">

  <section class="card card--front" aria-label="Card front">
    <div class="brand">
      <span class="brand__square"></span>
      <div class="brand__name">
        <span class="brand__main">Greenvale</span>
        <span class="brand__sub">Underwriting Pty Ltd</span>
      </div>
    </div>
  </section>

  <section class="card card--back" aria-label="Card back">
    <svg class="wave" viewBox="0 0 600 343" aria-hidden="true">
      <defs>
        <path id="wave-shape" d="M186,343 C300,330 320,240 370,160 C420,90 510,64 600,60 L640,60 L640,400 L186,400 Z"/>
      </defs>
      <use href="#wave-shape" fill="var(--lime)" transform="translate(-30,-14)"/>
      <use href="#wave-shape" fill="var(--paper)" transform="translate(-22,-10)"/>
      <use href="#wave-shape" fill="var(--citron)" transform="translate(-14,-6)"/>
      <use href="#wave-shape" fill="var(--paper)" transform="translate(-7,-3)"/>
      <use href="#wave-shape" fill="var(--forest)"/>
    </svg>

    <div class="brand">
      <span class="brand__square"></span>
      <div class="brand__name">
        <span class="brand__main">Greenvale</span>
        <span class="brand__sub">Underwriting Pty Ltd</span>
      </div>
    </div>

    <div class="contact">
      <p class="contact__name">Daniel Harrow</p>
      <p class="contact__title">President</p>
      <ul class="contact__list">
        <li>555-010-4821
          <svg class="icon" viewBox="0 0 12 12"><path d="M2 1 L4.5 1 L5.5 3.5 L4 4.8 C4.8 6.5 5.6 7.3 7.2 8 L8.5 6.5 L11 7.5 L11 10 C6 11 1 6 2 1 Z" fill="var(--citron)"/></svg>
        </li>
        <li>555-010-4822
          <svg class="icon" viewBox="0 0 12 12"><rect x="3" y="0.5" width="6" height="11" rx="1.2" fill="none" stroke="var(--citron)" stroke-width="1.3"/></svg>
        </li>
        <li>info@greenvaleuw.com
          <svg class="icon" viewBox="0 0 12 12"><rect x="0.5" y="2.5" width="11" height="7" fill="var(--citron)"/><path d="M0.5 2.5 L6 6.5 L11.5 2.5" fill="none" stroke="var(--forest)" stroke-width="1"/></svg>
        </li>
        <li>www.greenvaleuw.com
          <svg class="icon" viewBox="0 0 12 12"><circle cx="6" cy="6" r="5.5" fill="var(--citron)"/><path d="M0.5 6 H11.5 M6 0.5 C3 3 3 9 6 11.5 M6 0.5 C9 3 9 9 6 11.5" fill="none" stroke="var(--forest)" stroke-width="0.8"/></svg>
        </li>
      </ul>
    </div>
  </section>

</main>
</body>
</html>
```